Brochure Advertising Trademarks/copyrights/Fashion Law

**Trifold Brochure Description for Trademark and Legal Services in Fashion**

**Brochure Layout:**

### **Front Cover:**
- **Headline:** "Protect Your Vision. Elevate Your Brand."
- **Design:** Sleek and modern with a high-fashion vibe. A striking full-page image of a model on a runway, surrounded by geometric accents and minimalist typography. Incorporate your logo prominently.
- **Subhead:** "Expert Legal Solutions for the Fashion Industry"

### **Inside Panels (Three Main Sections):**

1. **Panel 1: Trademarks – Defend Your Brand Identity**
- **Visuals:** High-resolution image of a fashion designer's logo on a tag or luxury boutique storefront.
- **Content:**
- Explanation of trademarks and their importance in protecting brand identity.
- Real-world examples of trademark use in the fashion industry.
- Call-to-action: “Let us help you register and protect your brand globally.”

2. **Panel 2: Copyright – Safeguard Your Creative Works**
- **Visuals:** Artistic photo of a photographer working in a studio or a designer sketching a dress.
- **Content:**
- Importance of copyright for safeguarding original designs, photos, and marketing materials.
- Brief outline of the registration process.
- Call-to-action: “Your creativity deserves legal protection—consult us today.”

3. **Panel 3: Design Patents – Protect Your Innovative Styles**
- **Visuals:** Fashionable close-up of unique accessory designs, like a handbag or sunglasses.
- **Content:**
- Role of design patents in protecting innovative styles and functional designs.
- Examples relevant to accessories and footwear.
- Call-to-action: “Ensure your designs are protected from imitation.”

### **Back Panel:**

**About Me:**
- **Photo:** Professional, high-quality headshot that exudes confidence and style.
- **Bio Highlights:**
- Your unique qualifications, including your LLM in Fashion Law, global presentations, and experience in intellectual property law.
- Mention your specific experience working with models, designers, and photographers in protecting their creative assets.
- **Firm Information:**
- Name, logo, and tagline (e.g., “Protecting Your Creativity, One Step at a Time”).
- Contact information: phone, email, website, and social media handles.
- QR code linking to your website or consultation scheduling page.

**Closing Tagline:**
"Your Creativity, Your Vision, Protected by Experts."

**Design Notes:**
- Use a color palette inspired by high-fashion brands (e.g., black, white, gold, and nude tones).
- Include clean typography and minimalist accents.
- Highlight your expertise with an elegant yet approachable layout.

This brochure will capture attention and resonate with high-profile clients in the fashion industry.

How do I post my licensed images to be used in the brochure

Target Market(s)

Fashion Models, fashion Designers who may want a trademark

Industry/Entity Type

I am a lawyer serving the fashion industry offering intellectual property protection

Font styles to use
Serif
Sans Serif

Colors
E54698
E96AAD
F1A4CE
F9D9EA
FCEFF6

Requirements
Must have
• All pertinent information contained regarding the difference between trademark copyrights and patents and my bio.
Nice to have
• I would like to see a sleek fashionable but professional brochure with all of the information easy to read.
Should not have
• Amateur grammar or grammatical errors

```html
<!DOCTYPE html>
<html lang="en">
<head>
<meta charset="utf-8">
<title>Fashion Law Brochure – Inside Spread</title>
<link rel="stylesheet" href="https://fonts.googleapis.com/css2?family=EB+Garamond:ital,wght@0,400;0,500;1,400&family=Montserrat:wght@400;500;600&family=Open+Sans:wght@300;400&display=swap">
<style>
  :root {
    --pink-block: #dc4a9b;
    --magenta: #e6097f;
    --accent-pink: #e0318c;
    --dash-pink: #f1a4ce;
    --heading-grey: #4a4a4f;
    --body-grey: #3e3e42;
    --paper: #ffffff;
    --photo-light: #f4f3f1;
    --photo-mid: #e6e2dd;
    --photo-table: #c9c5c0;
  }
  * { margin: 0; padding: 0; box-sizing: border-box; }
  html, body { width: 1200px; height: 927px; overflow: hidden; background: var(--paper); }
  .spread { position: relative; width: 1200px; height: 927px; background: var(--paper); }

  .hero-quote {
    position: absolute; left: 0; top: 0; width: 349px; height: 368px;
    background: var(--pink-block);
  }
  .hero-quote p {
    position: absolute; left: 105px; top: 127px; width: 230px;
    font-family: "EB Garamond", serif; font-style: italic;
    font-size: 25.5px; line-height: 33.5px; color: #fff;
  }
  .hero-photo { position: absolute; left: 349px; top: 0; width: 851px; height: 368px; display: block; }

  .service {
    position: absolute; top: 368px; width: 400px; height: 559px;
  }
  .service--copyright { left: 400px; background: linear-gradient(90deg, #ededed 0, #f8f8f8 6px, #fff 22px); }
  .service--patents { left: 800px; background: linear-gradient(90deg, #ededed 0, #f8f8f8 6px, #fff 22px); }
  .service--trademarks { left: 0; }

  .service__title {
    position: absolute; left: 51px; top: 31px;
    font-family: "Montserrat", sans-serif; font-weight: 600;
    font-size: 22px; letter-spacing: 3.6px; line-height: 1; color: var(--heading-grey);
  }
  .service__tagline {
    position: absolute; left: 51px; top: 65px;
    font-family: "Montserrat", sans-serif; font-weight: 500;
    font-size: 7.4px; letter-spacing: 0.2px; color: var(--accent-pink);
  }
  .service__intro {
    position: absolute; left: 51px; top: 91px; width: 300px;
    font-family: "EB Garamond", serif; font-size: 11.6px; line-height: 16.7px; color: var(--body-grey);
  }
  .service__how {
    position: absolute; left: 51px; top: 224px;
    font-family: "Montserrat", sans-serif; font-weight: 500;
    font-size: 12px; letter-spacing: 1.8px; color: var(--accent-pink);
  }
  .step { position: absolute; left: 0; width: 400px; }
  .step__num {
    position: absolute; left: 51px; width: 31px; height: 31px; border-radius: 50%;
    background: var(--magenta); color: #fff;
    font-family: "Open Sans", sans-serif; font-weight: 300; font-size: 17px;
    line-height: 31px; text-align: center;
  }
  .step__text {
    position: absolute; left: 94px; width: 262px;
    font-family: "EB Garamond", serif; font-size: 11.6px; line-height: 16.7px; color: var(--body-grey);
  }
  .step__name { display: block; font-size: 11.8px; }
  .step--one   { top: 255px; }
  .step--two   { top: 340px; }
  .step--three { top: 426px; }
  .step--one .step__num   { top: 11px; }
  .step--two .step__num   { top: 18px; }
  .step--three .step__num { top: 19px; }

  .divider {
    position: absolute; left: 53px; width: 283px; height: 0;
    border-top: 1px dashed var(--dash-pink);
  }
  .divider--one { top: 330px; }
  .divider--two { top: 418px; }

  .service--patents .service__title,
  .service--patents .service__how { top: 29px; }
  .service--patents .service__how { top: 222px; }
  .service--patents .service__tagline { top: 63px; }
  .service--patents .service__intro { top: 89px; width: 292px; }
  .service--patents .step--one { top: 253px; }
  .service--copyright .service__intro { width: 290px; }
  .service--copyright .step__text { width: 250px; }
</style>
</head>
<body>
<main class="spread">
  <section class="hero-quote">
    <p>Let us help you register and protect your brand identity worldwide.</p>
  </section>

  <svg class="hero-photo" viewBox="0 0 851 368" role="img" aria-label="Photo of a bright fashion studio: a clothing rail of shirts, a sewing machine, a dress form in an orange dress, folded fabrics and colourful thread spools on a white table">
    <defs>
      <linearGradient id="studio-light" x1="0" y1="0" x2="0" y2="1">
        <stop offset="0" stop-color="#f6f5f3"/>
        <stop offset="0.7" stop-color="#ece8e4"/>
        <stop offset="1" stop-color="#d8d3ce"/>
      </linearGradient>
      <linearGradient id="studio-colour" x1="0" y1="0" x2="1" y2="0">
        <stop offset="0" stop-color="#e9c9c4" stop-opacity="0.35"/>
        <stop offset="0.45" stop-color="#f0f0ee" stop-opacity="0"/>
        <stop offset="0.62" stop-color="#d9643a" stop-opacity="0.25"/>
        <stop offset="0.8" stop-color="#f5f3f0" stop-opacity="0"/>
        <stop offset="1" stop-color="#7cc6dc" stop-opacity="0.35"/>
      </linearGradient>
    </defs>
    <rect width="851" height="368" fill="url(#studio-light)"/>
    <rect width="851" height="368" fill="url(#studio-colour)"/>
    <rect y="352" width="851" height="16" fill="var(--photo-table)"/>
  </svg>

  <article class="service service--trademarks">
    <h2 class="service__title">TRADEMARKS</h2>
    <p class="service__tagline">DEFEND YOUR BRAND IDENTITY</p>
    <p class="service__intro">Trademarks are the cornerstone of protecting your brand identity. In the fashion industry, where logos and branding hold immense value, trademarks ensure your brand stands apart in a competitive market. Whether it’s your logo on a designer tag or the name on a luxury storefront, trademarks safeguard what makes your brand unique.</p>
    <h3 class="service__how">HOW IT WORKS</h3>
    <div class="step step--one"><span class="step__num">1</span><p class="step__text"><span class="step__name">Initial Consultation</span>We begin with a thorough discussion to understand your brand identity, goals, and any existing assets.</p></div>
    <div class="divider divider--one"></div>
    <div class="step step--two"><span class="step__num">2</span><p class="step__text"><span class="step__name">Search and Analysis</span>Our team conducts a comprehensive trademark search to ensure your mark is unique and eligible for protection.</p></div>
    <div class="divider divider--two"></div>
    <div class="step step--three"><span class="step__num">3</span><p class="step__text"><span class="step__name">Registration and Monitoring</span>Once approved, we file your application and provide ongoing monitoring to guard against potential infringement.</p></div>
  </article>

  <article class="service service--copyright">
    <h2 class="service__title">COPYRIGHT</h2>
    <p class="service__tagline">SAFEGUARD YOUR CREATIVE WORKS</p>
    <p class="service__intro">Your creativity is your greatest asset. Copyright law protects your original designs, photos, and marketing materials, ensuring they remain yours. From the intricate details of a designer sketch to the artistry of a professional photoshoot, copyright safeguards the essence of your brand’s creativity.</p>
    <h3 class="service__how">HOW IT WORKS</h3>
    <div class="step step--one"><span class="step__num">1</span><p class="step__text"><span class="step__name">Assessment</span>We identify which creative works are eligible for copyright protection, from designs to marketing materials.</p></div>
    <div class="divider divider--one"></div>
    <div class="step step--two"><span class="step__num">2</span><p class="step__text" style="top:-2px"><span class="step__name">Registration</span>We file copyright applications with the appropriate authorities to secure your intellectual property.</p></div>
    <div class="divider divider--two"></div>
    <div class="step step--three"><span class="step__num">3</span><p class="step__text"><span class="step__name">Enforcement</span>If your rights are violated, we provide legal strategies to enforce your copyrights and pursue claims against infringers.</p></div>
  </article>

  <article class="service service--patents">
    <h2 class="service__title">DESIGN PATENTS</h2>
    <p class="service__tagline">PROTECT YOUR INNOVATIVE STYLES</p>
    <p class="service__intro">In the fashion world, innovation takes many forms—whether it’s a cutting-edge handbag design or a unique pair of sunglasses. Design patents ensure your innovative styles are legally protected from imitation, allowing you to maintain exclusivity in the market.</p>
    <h3 class="service__how">HOW IT WORKS</h3>
    <div class="step step--one"><span class="step__num">1</span><p class="step__text" style="left:91px"><span class="step__name">Idea Validation</span>We evaluate whether your design meets the criteria for patent protection.</p></div>
    <div class="divider divider--one"></div>
    <div class="step step--two"><span class="step__num">2</span><p class="step__text" style="left:91px;top:-1px"><span class="step__name">Application Filing</span>We prepare and file detailed applications, including design drawings and specifications.</p></div>
    <div class="divider divider--two"></div>
    <div class="step step--three"><span class="step__num">3</span><p class="step__text" style="left:91px;top:1px"><span class="step__name">Enforcement</span>Once your design patent is granted, we help enforce your rights against unauthorized use.</p></div>
  </article>
</main>
</body>
</html>
```